Business Card Design

We need a business card for a well established Semi Trailer Hire company. I am looking for a new start as we are moving so would like to update our Business Cards and Letter heads.
We hire Semi Trailers to Transport companies.
The colour of our Trailers are Cherry Red so this must be the prominent colour.
I do not want any pictures of trailers on the design.
I do not want the design to be flowery in anyway as we are in the transport industry.
Simple yet effective

Business

Varno Tolt Hire Pty Ltd
Ros Penbury
Director
Ph: 03 9412 5038
Mobile: 0427 836 207
ros.penbury@varnotolt-example.com.au
www.varnotolt-example.com.au
218-224 Dunmore Road, Callowvale

```html
<!DOCTYPE html>
<html lang="en">
<head>
<meta charset="utf-8">
<title>Varno Tolt Hire – Business Card</title>
<link rel="stylesheet" href="https://fonts.googleapis.com/css2?family=Lato:wght@400;700&display=swap">
<style>
  :root {
    --cherry: #8e1616;
    --cream: #efe1b9;
    --ink: #141414;
    --band: #000000;
    --backdrop: #d9d9d9;
  }
  * { margin: 0; padding: 0; box-sizing: border-box; }
  html, body {
    width: 1200px;
    height: 926px;
    overflow: hidden;
    background: var(--backdrop);
    font-family: "Lato", Arial, sans-serif;
  }
  .canvas {
    position: relative;
    width: 1200px;
    height: 926px;
  }
  .card {
    position: absolute;
    left: 250px;
    width: 700px;
    height: 400px;
    background: var(--cream);
    box-shadow: 0 2px 6px rgba(0,0,0,0.18);
  }
  .card--front { top: 42px; }
  .card--back { top: 484px; }

  .holder-name {
    position: absolute;
    left: 44px;
    top: 80px;
    font-size: 36px;
    line-height: 1;
    color: var(--cherry);
    font-weight: 400;
    letter-spacing: 0.5px;
  }
  .holder-name strong { font-weight: 700; }

  .title-band {
    position: absolute;
    left: 0;
    top: 126px;
    width: 440px;
    height: 40px;
    background: var(--band);
  }
  .holder-role {
    position: absolute;
    left: 46px;
    top: 3px;
    font-size: 14px;
    letter-spacing: 1px;
    color: var(--cherry);
    text-transform: uppercase;
  }

  .contact-list {
    position: absolute;
    left: 42px;
    top: 188px;
    list-style: none;
    font-size: 17px;
    line-height: 23px;
    color: var(--ink);
  }
  .contact-list .label {
    color: var(--cherry);
    font-weight: 700;
    margin-right: 4px;
  }

  .company-vertical {
    position: absolute;
    right: 28px;
    top: 0;
    height: 400px;
    display: flex;
    align-items: center;
    justify-content: center;
    writing-mode: vertical-rl;
    transform: rotate(180deg);
    font-size: 28px;
    font-weight: 700;
    color: var(--cherry);
    letter-spacing: 0.3px;
  }

  .company-centre {
    position: absolute;
    inset: 0;
    display: flex;
    align-items: center;
    justify-content: center;
    font-size: 30px;
    font-weight: 700;
    color: var(--cherry);
    letter-spacing: 0.3px;
  }
</style>
</head>
<body>
<main class="canvas">
  <section class="card card--front" aria-label="Business card front">
    <h1 class="holder-name">ROS <strong>PENBURY</strong></h1>
    <div class="title-band">
      <span class="holder-role">Director</span>
    </div>
    <ul class="contact-list">
      <li><span class="label">phone:</span>03 9412 5038</li>
      <li><span class="label">mobile:</span>0427 836 207</li>
      <li><span class="label">email:</span>ros.penbury@varnotolt-example.com.au</li>
      <li><span class="label">web:</span>www.varnotolt-example.com.au</li>
      <li><span class="label">address:</span>218-224 Dunmore Road, Callowvale</li>
    </ul>
    <p class="company-vertical">VARNO TOLT HIRE Pty Ltd</p>
  </section>

  <section class="card card--back" aria-label="Business card back">
    <p class="company-centre">VARNO TOLT HIRE Pty Ltd</p>
  </section>
</main>
</body>
</html>
```